Outdoor mass notification company needing business card design.

Our company name is Harborline Signal Systems Inc located in Amory Mississippi and we sell and maintain "Corvath" Mass Notification Sirens in the US. Outdoor sirens notify people of certain severe dangers such as tornados, severe thunderstorms, flooding, hurricanes and tsunamis. We also serve the oil and gas refining industries to warn of Chemical releases, fires, and lightning alerts.

Contact Information for Business Card

Name, title, cell number, email address

Requirements
Nice to have
• The Corvath logo and also the Tallbrook logo.

```html
<!DOCTYPE html>
<html lang="en">
<head>
<meta charset="utf-8">
<title>Harborline Signal Systems – Business Card</title>
<link href="https://fonts.googleapis.com/css2?family=Arimo:wght@400;700&display=swap" rel="stylesheet">
<style>
  :root {
    --page-bg: #eeebe7;
    --card-light: #e9e5df;
    --card-mid: #d9d3cb;
    --navy-dark: #1d2431;
    --navy: #2f3a4c;
    --name-tan: #dccdb9;
    --ink: #272a30;
    --ink-soft: #3a3e46;
    --hairline: rgba(255,255,255,0.55);
  }
  * { margin: 0; padding: 0; box-sizing: border-box; }
  html, body {
    width: 1170px; height: 1200px; overflow: hidden;
    background: var(--page-bg);
    font-family: "Arimo", Arial, sans-serif;
  }
  .business-card {
    position: absolute; left: 60px; top: 300px;
    width: 1050px; height: 598px;
    border-radius: 30px; overflow: hidden;
    background: linear-gradient(160deg, var(--card-light), var(--card-mid));
    box-shadow: 0 0 0 1.5px rgba(40,44,52,0.35), 0 14px 40px rgba(0,0,0,0.12);
  }
  .card-shapes { position: absolute; inset: 0; }
  .holder-name {
    position: absolute; left: 63px; top: 50px;
    font-size: 37px; font-weight: 700; color: var(--name-tan); letter-spacing: 0.2px;
  }
  .holder-title {
    position: absolute; left: 65px; top: 96px;
    font-size: 24px; color: var(--name-tan);
  }
  .company-name {
    position: absolute; right: 62px; top: 88px; text-align: right;
    font-weight: 700; color: var(--ink); line-height: 1.05;
  }
  .company-name .line-one { display: block; font-size: 40px; letter-spacing: 1px; }
  .company-name .line-two { display: block; font-size: 29px; letter-spacing: 1.4px; }
  .address {
    position: absolute; left: 63px; top: 340px;
    font-size: 25px; line-height: 32px; color: var(--ink);
  }
  .contact-list {
    position: absolute; left: 63px; top: 437px; list-style: none;
    font-size: 25px; line-height: 33px; color: var(--ink-soft);
  }
  .contact-list li { display: flex; align-items: center; gap: 12px; }
  .contact-list svg { width: 22px; height: 22px; fill: var(--ink-soft); flex: none; }
</style>
</head>
<body>
  <div class="business-card">
    <svg class="card-shapes" viewBox="0 0 1050 598" width="1050" height="598" aria-hidden="true">
      <defs>
        <linearGradient id="navyFill" x1="0" y1="0" x2="1" y2="1">
          <stop offset="0" stop-color="var(--navy)"/>
          <stop offset="1" stop-color="var(--navy-dark)"/>
        </linearGradient>
      </defs>
      <polygon class="corner-band-top" points="0,0 515,0 276,111 350,148 0,262" fill="url(#navyFill)"/>
      <polyline class="accent-hairline" points="658,598 770,485 818,508 1050,398" fill="none" stroke="var(--hairline)" stroke-width="1.2"/>
      <polygon class="corner-band-bottom" points="1050,398 1050,598 658,598 913,517 857,492" fill="url(#navyFill)"/>
    </svg>

    <div class="holder-name">Owen Castell</div>
    <div class="holder-title">President</div>

    <div class="company-name">
      <span class="line-one">HARBORLINE</span>
      <span class="line-two">SIGNAL SYSTEMS</span>
    </div>

    <div class="address">
      412 Meridian Row<br>
      Amory, MS 38821
    </div>

    <ul class="contact-list">
      <li>
        <svg viewBox="0 0 24 24"><path d="M6.6 2.5l3 3.3c.5.5.5 1.3 0 1.8L8 9.3c1.2 2.6 3.9 5.3 6.7 6.7l1.7-1.6c.5-.5 1.3-.5 1.8 0l3.3 3c.5.5.5 1.3 0 1.8l-1.9 1.9c-.9.9-2.3 1.1-3.4.5C9.7 19 5 14.3 2.4 7.8c-.6-1.1-.4-2.5.5-3.4L4.8 2.5c.5-.5 1.3-.5 1.8 0z"/></svg>
        (662) 5190-3378
      </li>
      <li>
        <svg viewBox="0 0 24 24"><path d="M2 6h20v13H2z M3.5 7.5L12 13l8.5-5.5" fill="var(--ink-soft)" stroke="var(--card-light)" stroke-width="1.4"/></svg>
        name@harborlinesignal.com
      </li>
      <li>
        <svg viewBox="0 0 24 24"><circle cx="12" cy="12" r="10"/><path d="M7 7c2 0 3 1 3 3s-2 2-2 4 2 2 2 5M14 4c0 2 1 3 3 3s3 2 2 4-3 1-4 3 1 4 0 6" fill="none" stroke="var(--card-light)" stroke-width="1.5"/></svg>
        www.harborlinesignal.com
      </li>
    </ul>
  </div>
</body>
</html>
```